Brightvantage.com tech company website

Current site is www.brightvantage.com. The site will tell you about our company.

Designs we like are:
http://megainfo.quellorix.com
www.trelvo.com
www.morvasket.com

Target Market(s)

B2B

Industry/Entity Type

It Company

Coding

Coded - Design and coding required

Number of Pages Required

5+ page

Requirements
Must have
• We want to entice without giving away too much info. We like graphics and colors. But website must look official and credible.

```html
<!DOCTYPE html>
<html lang="en">
<head>
<meta charset="utf-8">
<title>Brightvantage</title>
<link href="https://fonts.googleapis.com/css2?family=Open+Sans:wght@400;600;700&display=swap" rel="stylesheet">
<style>
:root{
  --navy:#143a64;
  --blue:#1f6fb2;
  --sky:#3f9ad8;
  --ink:#333a42;
  --muted:#8a929a;
  --line:#e3e6ea;
  --grey:#eef0f2;
  --footer:#1e2226;
  --footer-text:#9aa1a8;
  --orange:#f5a623;
  --white:#ffffff;
}
*{box-sizing:border-box;margin:0;padding:0}
html,body{width:898px;height:1200px;overflow:hidden}
body{font-family:"Open Sans",Arial,sans-serif;color:var(--ink);background:var(--white);position:relative}
.topbar{height:14px;background:var(--navy);display:flex;justify-content:flex-end;gap:14px;padding:0 40px;font-size:6px;color:#cfe0f0;align-items:center;letter-spacing:.5px}
.header{height:76px;display:flex;align-items:center;padding:0 40px;border-bottom:1px solid var(--line)}
.brand{display:flex;align-items:center;gap:8px;font-weight:700;font-size:17px;color:var(--navy);letter-spacing:.5px}
.brand-mark{width:14px;height:14px;background:var(--blue)}
.nav{margin-left:auto;display:flex;gap:44px;font-size:11px;color:var(--blue);font-weight:600;margin-right:60px}
.hero{height:240px;background:linear-gradient(120deg,#0d3d6b 0%,#2477b8 55%,#5cb4e6 100%);display:flex;flex-direction:column;align-items:center;padding-top:95px;color:var(--white)}
.hero h1{font-size:17px;font-weight:600;text-align:center;line-height:1.3;letter-spacing:.5px;width:340px}
.hero .rule{width:60px;height:1px;background:rgba(255,255,255,.6);margin-top:12px}
.feature{position:absolute;left:120px;top:285px;width:660px;height:205px;background:var(--white);box-shadow:0 2px 10px rgba(0,0,0,.12);display:flex;align-items:center;padding:0 36px;gap:34px}
.feature-art{width:200px;height:130px;background:linear-gradient(160deg,#d8dde2,#f1f3f5);border-radius:4px}
.feature h2{font-size:15px;color:var(--navy);font-weight:600;margin-bottom:10px}
.feature p{font-size:8px;line-height:1.6;color:var(--muted);width:340px}
.link{display:inline-block;margin-top:14px;font-size:7px;color:var(--blue);font-weight:700;letter-spacing:.5px}
.services{position:absolute;top:510px;left:135px;width:640px;display:flex;justify-content:space-between}
.service{width:190px;display:flex;gap:10px}
.service svg{flex:none}
.service h3{font-size:10px;font-weight:600;color:var(--ink);margin-bottom:5px}
.service ul{list-style:none;font-size:7px;color:var(--muted);line-height:1.6}
.btn{display:inline-block;margin-top:8px;background:var(--navy);color:var(--white);font-size:6.5px;padding:5px 11px;border-radius:2px;letter-spacing:.5px}
.divider{position:absolute;top:645px;left:0;width:898px;height:1px;background:var(--line)}
.cloud{position:absolute;top:690px;left:0;width:898px;display:flex;padding:0 125px;gap:55px;align-items:center}
.cloud-art{width:270px;height:160px;background:radial-gradient(ellipse at 50% 40%,#fbd27a,#fdeccb 55%,#f5f7f9 80%);border-radius:6px}
.cloud h2{font-size:13px;color:var(--navy);font-weight:600;margin-bottom:6px}
.cloud .lead{font-size:7.5px;color:var(--blue);font-weight:600;margin-bottom:8px;line-height:1.5}
.cloud p{font-size:7.5px;color:var(--muted);line-height:1.6;width:320px}
.btn-outline{display:inline-block;margin-top:14px;border:1px solid var(--ink);font-size:6.5px;padding:5px 12px;color:var(--ink);letter-spacing:.5px}
.band{position:absolute;top:900px;left:0;width:898px;height:150px;background:var(--grey);text-align:center;padding-top:30px}
.band h2{font-size:17px;color:var(--blue);font-weight:400;letter-spacing:1px;margin-bottom:10px}
.band p{font-size:7.5px;color:var(--muted);line-height:1.6;width:420px;margin:0 auto}
.band .btn{margin-top:12px;background:var(--blue);padding:6px 14px}
.footer{position:absolute;top:1065px;left:0;width:898px;height:135px;background:var(--footer);display:flex;padding:30px 175px 0;gap:60px;color:var(--footer-text)}
.footer h4{font-size:8px;color:var(--white);font-weight:700;letter-spacing:.5px;margin-bottom:8px}
.footer p,.footer li{font-size:6.5px;line-height:1.7;list-style:none}
.phone{font-size:10px;color:var(--white);margin-top:6px}
.social{display:flex;gap:10px;margin-left:auto}
.social span{width:18px;height:18px;border-radius:50%;background:#4a5058}
</style>
</head>
<body>
<div class="topbar"><span>HOME</span><span>ABOUT US</span><span>CONTACT</span></div>
<header class="header">
  <div class="brand"><span class="brand-mark"></span>BRIGHTVANTAGE</div>
  <nav class="nav"><span>Big Data &amp; Analytics</span><span>Reception &amp; Influence</span><span>Case Studies</span></nav>
</header>

<section class="hero" role="img" aria-label="Hand touching a glowing blue digital interface">
  <h1>GREAT SERVICES AND EXPERTISE IN EVERYTHING WE DO</h1>
  <div class="rule"></div>
</section>

<section class="feature">
  <div class="feature-art" role="img" aria-label="Laptop with colourful data analytics bubbles"></div>
  <div>
    <h2>Big Data Analytics</h2>
    <p>We turn complex data into clear insight so your teams can act faster. Our analytics platform connects every source, finds patterns that matter and delivers reports your leaders trust, all in one secure place.</p>
    <span class="link">READ MORE</span>
  </div>
</section>

<section class="services">
  <div class="service">
    <svg width="22" height="22" viewBox="0 0 22 22"><rect x="3" y="5" width="16" height="11" fill="none" stroke="#8a929a" stroke-width="1.5"/><line x1="8" y1="19" x2="14" y2="19" stroke="#8a929a" stroke-width="1.5"/></svg>
    <div><h3>Web Service</h3>
      <ul><li>Cloud Solutions</li><li>Application Hosting &amp; Support</li><li>Migration</li><li>Data Integration</li><li>Custom Software Design</li></ul>
      <span class="btn">READ MORE</span></div>
  </div>
  <div class="service">
    <svg width="22" height="22" viewBox="0 0 22 22"><circle cx="11" cy="11" r="8" fill="none" stroke="#8a929a" stroke-width="1.5"/><path d="M11 6v5l3 3" fill="none" stroke="#8a929a" stroke-width="1.5"/></svg>
    <div><h3>Case Studies</h3>
      <ul><li>Retail Data Platform</li><li>Financial Risk Insight</li><li>Logistics Dashboard</li><li>Health Record Analytics</li><li>Marketing Reach Review</li></ul>
      <span class="btn">READ MORE</span></div>
  </div>
  <div class="service">
    <svg width="22" height="22" viewBox="0 0 22 22"><path d="M4 17l5-6 4 3 5-8" fill="none" stroke="#8a929a" stroke-width="1.5"/></svg>
    <div><h3>Analytics</h3>
      <ul><li>Business Insight</li><li>Predictive Modelling</li><li>Customer Behaviour Trends</li><li>Social Media Reach</li><li>Live Reporting</li></ul>
      <span class="btn">READ MORE</span></div>
  </div>
</section>

<div class="divider"></div>

<section class="cloud">
  <div class="cloud-art" role="img" aria-label="Orange clouds connected to laptop, tablet and phone"></div>
  <div>
    <h2>Experienced in complete web ease</h2>
    <div class="lead">Complete cloud services that scale with your business needs every day</div>
    <p>From planning to launch, our specialists manage infrastructure, security and performance so your systems stay fast and available. We keep things simple, transparent and ready for growth.</p>
    <span class="btn-outline">LEARN MORE</span>
  </div>
</section>

<section class="band">
  <h2>BIG DATA ANALYTICS</h2>
  <p>Discover what your information can do for you. Our team builds tools that reveal trends, reduce risk and guide smarter decisions across your whole organisation.</p>
  <span class="btn">CONTACT US</span>
</section>

<footer class="footer">
  <div><h4>BRIGHTVANTAGE</h4><p>Smarter data for business</p></div>
  <div><h4>ONLINE SUPPORT</h4>
    <svg width="16" height="16" viewBox="0 0 16 16"><rect x="2" y="2" width="12" height="12" fill="#3f9ad8"/></svg>
    <div class="phone">+1 800 555 01 47</div>
    <p>help@brightvantage.com</p></div>
  <div><h4>SITE LINK</h4><ul><li>Home</li><li>About Us</li><li>Services</li><li>Case Studies</li><li>Contact</li></ul></div>
  <div class="social"><span></span><span></span><span></span></div>
</footer>
</body>
</html>
```